Design a Wholefood grain/rice packaging

To design an outer box for a Rice/grains product. It will be vacumm packed in 1 kg size and see through plastic bag and inserted into an outer box. The outer box will need designing to appeal to consumer to buy. The rice/grain product will be sold in healthfood store or supermarkets. Design layout must give it a feel like it is premium, natural, wholesome and easy to read. Please pay more attention to the back detail for instruction, usage or recommended recipes.

Target Market(s)

30-70 years old (both male and female) who like to stay healthy in their food choices, maybe a vegan customer. Shops in supermarkets that offers organic food products.

Industry/Entity Type

Plastic

Font styles to use
Serif

Colors

Designer to choose colors to be used in the design.

Requirements
Must have
• Visuals that appeal to health conscious customers. Must look 'fresh' and 'natural'. Colours can have toning/shading effect to make it more visually appealing (like rainbow colours) or could just have more white background to give it a simple and clean look. Text and fonts style used is important to ensure it looks 'western' feel.
Nice to have
• Pictures of the actual rice cooked ( We can take a picture of our product in cooked form to show the consumer how it looks like after it is cooked). Space to show recommended recipe, steps 1-4 on how to cook, some information on why grains can help benefit one's health.
Should not have
• Should not have visuals on religious signs, animals. Should not have strong single colours. Text must be easily readible to the consumer.

```html
<!DOCTYPE html>
<html lang="en">
<head>
<meta charset="utf-8">
<title>Harvest Grains Rice – Box Panels</title>
<link href="https://fonts.googleapis.com/css2?family=Archivo+Black&family=Montserrat:wght@600;700&family=Open+Sans:wght@400&family=Oswald:wght@300&display=swap" rel="stylesheet">
<style>
  :root{
    --bg:#e9e9e9;
    --cream:#f8f7dc;
    --cream-deep:#eeeab0;
    --leaf:#7fbf1f;
    --leaf-light:#9bd13a;
    --leaf-dark:#4f8f16;
    --forest:#25704b;
    --white:#ffffff;
    --stripe-a:#9ed257;
    --stripe-b:#5fa924;
  }
  *{box-sizing:border-box;margin:0;padding:0}
  html,body{width:1200px;height:1200px;overflow:hidden}
  body{background:var(--bg);position:relative;font-family:"Montserrat",sans-serif}

  .panel{position:absolute;top:110px;height:980px;overflow:hidden}

  /* side panel */
  .side-panel{left:60px;width:260px;
    background:linear-gradient(180deg,var(--cream) 0%,var(--cream) 55%,#cfe79a 75%,var(--stripe-a) 100%)}
  .ingredients{position:absolute;left:12px;top:70px;width:238px;padding:14px 12px 16px;
    background:linear-gradient(135deg,var(--leaf-light),var(--leaf-dark));
    border:1px solid var(--leaf-dark);color:var(--white);
    font-family:"Open Sans",sans-serif;font-size:14px;line-height:1.75;white-space:nowrap}
  .ingredients li{list-style:none}

  /* front panel */
  .front-panel{left:320px;width:820px;
    background:linear-gradient(180deg,var(--cream) 0%,var(--cream) 48%,#dcedae 60%,var(--stripe-a) 75%,var(--stripe-b) 100%)}

  .brand{position:absolute;left:48px;top:60px;width:230px;height:230px;border-radius:50%;
    background:var(--forest);border:6px solid var(--cream-deep);
    display:flex;align-items:center;justify-content:center}
  .brand-name{color:var(--white);font-weight:700;font-size:30px;letter-spacing:1px}

  .nutrition{position:absolute;right:30px;top:40px;display:flex;gap:6px;align-items:flex-start}
  .nutrition svg{display:block}
  .nutrient-label{font-family:"Montserrat",sans-serif;font-weight:600;font-size:14px;fill:var(--white)}
  .nutrient-label.small{font-size:12px}
  .nutrient-value{font-family:"Montserrat",sans-serif;font-weight:700;font-size:22px;fill:var(--white)}
  .energy-value{font-family:"Archivo Black",sans-serif;font-size:54px;fill:var(--white)}

  .title{position:absolute;left:190px;top:400px;color:var(--leaf)}
  .title-sub{font-weight:700;font-size:48px;display:block;margin-left:8px;white-space:nowrap}
  .title-main{font-family:"Archivo Black",sans-serif;font-size:170px;line-height:0.9;display:block}

  .organic-seal{position:absolute;left:580px;top:392px}

  .cooked-photo{position:absolute;left:40px;top:640px;width:500px;height:330px;
    border-radius:50% 50% 45% 45%/40% 40% 60% 60%;
    background:radial-gradient(ellipse at 50% 55%,#e7c3a4 0%,#c98f6e 45%,#8a4a36 75%,#f3f3f3 77%,#ffffff 100%)}
  .raw-grains{position:absolute;left:560px;top:620px}

  .net-weight{position:absolute;right:50px;bottom:40px;font-family:"Oswald",sans-serif;font-weight:300;
    font-size:40px;color:var(--cream-deep);white-space:nowrap}
</style>
</head>
<body>

  <section class="panel side-panel">
    <ul class="ingredients">
      <li>Brown Rice (Thailand)</li>
      <li>Red Rice UKMRC9 (Malaysian)</li>
      <li>Black Rice (Thailand)</li>
      <li>White Quinoa</li>
      <li>Total weight per serve (1kg)</li>
    </ul>
  </section>

  <section class="panel front-panel">
    <div class="brand"><span class="brand-name">Mira Grove</span></div>

    <div class="nutrition">
      <svg width="100" height="118" viewBox="0 0 100 118">
        <path d="M3 3H97V80Q97 115 50 115Q3 115 3 80Z" fill="var(--leaf)" stroke="var(--white)" stroke-width="4"/>
        <text class="nutrient-label small" x="50" y="22" text-anchor="middle">Total Energy</text>
        <text class="energy-value" x="50" y="84" text-anchor="middle">88</text>
        <text class="nutrient-label" x="50" y="104" text-anchor="middle" style="font-size:11px">Calories</text>
      </svg>
      <svg width="82" height="96" viewBox="0 0 82 96">
        <path d="M3 3H79V62Q79 93 41 93Q3 93 3 62Z" fill="var(--leaf)" stroke="var(--white)" stroke-width="4"/>
        <text class="nutrient-label" x="41" y="24" text-anchor="middle">Vitamin</text>
        <text class="nutrient-value" x="41" y="70" text-anchor="middle">4%</text>
      </svg>
      <svg width="82" height="96" viewBox="0 0 82 96">
        <path d="M3 3H79V62Q79 93 41 93Q3 93 3 62Z" fill="var(--leaf)" stroke="var(--white)" stroke-width="4"/>
        <text class="nutrient-label" x="41" y="24" text-anchor="middle">Natrium</text>
        <text class="nutrient-value" x="41" y="70" text-anchor="middle">11%</text>
      </svg>
      <svg width="82" height="96" viewBox="0 0 82 96">
        <path d="M3 3H79V62Q79 93 41 93Q3 93 3 62Z" fill="var(--leaf)" stroke="var(--white)" stroke-width="4"/>
        <text class="nutrient-label" x="41" y="24" text-anchor="middle">Kalsium</text>
        <text class="nutrient-value" x="41" y="70" text-anchor="middle">4%</text>
      </svg>
    </div>

    <h1 class="title">
      <span class="title-sub">Harvest Grains</span>
      <span class="title-main">RICE</span>
    </h1>

    <svg class="organic-seal" width="86" height="86" viewBox="0 0 86 86" aria-hidden="true">
      <circle cx="43" cy="43" r="40" fill="var(--leaf-dark)" stroke="var(--white)" stroke-width="3"/>
    </svg>

    <div class="cooked-photo" role="img" aria-label="Photo of cooked mixed brown, red and black rice in a white heart-shaped bowl"></div>

    <svg class="raw-grains" width="240" height="230" viewBox="0 0 240 230" role="img" aria-label="Close-up photo of uncooked mixed rice grains and quinoa inside a heart frame">
      <defs>
        <radialGradient id="grainTone" cx="50%" cy="45%" r="60%">
          <stop offset="0%" stop-color="#6b5a52"/>
          <stop offset="100%" stop-color="#2e2624"/>
        </radialGradient>
      </defs>
      <path d="M120 220C40 160 6 120 6 70C6 32 34 8 68 8C92 8 110 22 120 42C130 22 148 8 172 8C206 8 234 32 234 70C234 120 200 160 120 220Z"
            fill="url(#grainTone)" stroke="var(--leaf)" stroke-width="8"/>
    </svg>

    <p class="net-weight">Net Weight 1 kg</p>
  </section>

</body>
</html>
```